BramliVex a new start up looking for packaging design for it's organic Cold pressed Peanut oil.

We require a labelling design for a new company based in the UK called ''BramliVex''. We will be launching Organic cold pressed peanut oil. We would like a design that is simple yet very catchy and not boring.

Target Market(s)
General consumers and healthy eaters, Vegan friendly

Colors
Designer to choose colors to be used in the design.

Must have
• Refer to Packaging document information for labelling.
• Type of bottle 250 ML Selvane bottle (refer to Bottle Picture doc.)
• Must have the "BramliVex" logo stamped somewhere on the front of the package (refer to the Logo document)
• Sleek and appetising design
• Neutral colors possible accents with logo colors
• Claims: Organic, Vegan, High in Monounsaturated fat, High in Poly-unsaturated fat(all this in front of the package)
• Made in the uk logo, and EU organic logo
• Social Media Icons (Pictaloom,Chatterdesk) as well as website (Bramlivex.co.uk)
• Space reserved at the back of the package for barcode and best before date to be printed on.
Be nice to have: picture of the product on the background if possible
Updates

Need extra days to review

Target Market(s)

Font styles to use
Serif
Sans Serif
Decorative
Script

Requirements
Must have

• • Refer to Packaging document information for labelling.

```html
<!DOCTYPE html>
<html lang="en">
<head>
<meta charset="utf-8">
<title>BramliVex Organic Cold Pressed Peanut Oil – Label</title>
<link rel="stylesheet" href="https://fonts.googleapis.com/css2?family=Didact+Gothic&family=Titan+One&family=Fjalla+One&display=swap">
<style>
  :root {
    --paper: #ffffff;
    --sand: #e5c4a6;
    --cocoa: #3e1510;
    --brown: #7a4525;
    --mocha: #6e4a30;
    --toffee: #a0703c;
    --leaf: #7bb33a;
    --eu-green: #8cc43f;
    --steel-dark: #8d8d8f;
    --steel-light: #f2f2f2;
  }
  * { box-sizing: border-box; margin: 0; padding: 0; }
  html, body { width: 1200px; height: 1200px; overflow: hidden; background: var(--paper); }
  body { font-family: "Didact Gothic", sans-serif; color: var(--mocha); }
  .label { position: relative; width: 1200px; height: 1200px; background: var(--paper); overflow: hidden; }
  .abs { position: absolute; }

  .label-body { left: 0; top: 260px; width: 1200px; height: 823px; background: var(--sand); }
  .label-arch { left: 363px; top: 31px; width: 475px; height: 300px; background: var(--sand); border-radius: 237.5px 237.5px 0 0; }
  .metal-band { left: 0; top: 1083px; width: 1200px; height: 117px;
    background: linear-gradient(90deg, var(--steel-dark) 0%, var(--steel-light) 22%, #a9a9ab 45%, var(--steel-light) 70%, var(--steel-dark) 100%); }

  .brand-name { left: 363px; width: 475px; top: 100px; text-align: center;
    font-family: "Titan One", sans-serif; font-size: 62px; line-height: 1; color: var(--cocoa); }
  .mascot-art { left: 520px; top: 176px; width: 160px; height: 210px; border-radius: 24px;
    background: linear-gradient(180deg, #6a3420, #4a2014); }

  .social { left: 47px; display: flex; align-items: center; gap: 14px; font-size: 31px; color: var(--mocha); }
  .social-mark { width: 50px; height: 50px; border-radius: 8px; background: var(--brown); }

  .eu-organic { left: 143px; top: 518px; width: 107px; height: 72px; background: var(--eu-green); }

  .info-box { left: 40px; width: 313px; border-radius: 28px; padding: 14px 14px; white-space: nowrap; }
  .info-box h2 { font-weight: 400; line-height: 1.15; margin-bottom: 2px; }
  .info-box p { font-size: 25.5px; line-height: 32px; }
  .allergy { top: 623px; height: 272px; background: var(--toffee); color: var(--cocoa); padding-top: 20px; }
  .allergy h2 { font-size: 32px; }
  .storage { top: 907px; height: 155px; background: var(--cocoa); color: var(--sand); padding-top: 12px; }
  .storage h2 { font-size: 30px; color: #e9cfa9; }

  .claim-organic { left: 300px; width: 600px; top: 444px; text-align: center;
    font-family: "Titan One", sans-serif; font-size: 44px; letter-spacing: 1px; color: var(--brown); }
  .claim-process { left: 300px; width: 600px; top: 496px; text-align: center; font-size: 46px; color: var(--mocha); }
  .product-name { left: 300px; width: 600px; top: 560px; text-align: center;
    font-family: "Titan One", sans-serif; font-size: 75px; line-height: 1; color: var(--cocoa); }
  .peanut-art { left: 478px; top: 677px; width: 240px; height: 258px; border-radius: 24px;
    background: linear-gradient(160deg, #6f9a4c 0%, #a88a5e 55%, #a85a45 100%); opacity: 0.85; }

  .badge { text-align: center; font-family: "Fjalla One", sans-serif; color: var(--leaf); line-height: 0.95; }
  .badge span { display: block; }
  .badge-vegan { left: 492px; width: 94px; top: 978px; }
  .badge-vegan .b-top { font-size: 18px; }
  .badge-vegan .b-main { font-size: 38px; }
  .badge-vegan .b-sub { font-size: 20px; }
  .badge-organic { left: 612px; width: 104px; top: 998px; }
  .badge-organic .b-main { font-size: 32px; }
  .badge-organic .b-sub { font-size: 31px; }

  .uk-mark { left: 415px; top: 1092px; width: 70px; height: 70px; border-radius: 50%; background: #2b2b3a; border: 4px solid #fff; }
  .volume { left: 520px; width: 160px; top: 1106px; text-align: center; font-family: "Titan One", sans-serif; font-size: 33px; color: var(--cocoa); }

  .ingredients { left: 850px; width: 304px; top: 305px; text-align: center; font-size: 36px; line-height: 40px; color: var(--mocha); }

  .nutrition { left: 844px; top: 470px; width: 317px; }
  .nutrition h3 { font-weight: 400; font-size: 31px; color: var(--cocoa); margin-left: 4px; margin-bottom: 2px; }
  .nutrition table { width: 100%; border-collapse: collapse; font-size: 16.5px; color: var(--mocha); }
  .nutrition td { height: 24px; padding: 0 3px; }
  .nutrition td:last-child { text-align: right; }
  .nutrition .bar td { background: var(--brown); color: var(--cocoa); height: 22px; }
  .nutrition .sub td:first-child { padding-left: 13px; }
  .nutrition .sub2 td:first-child { padding-left: 18px; }
  .nutrition .strong td { color: var(--cocoa); }
  .nutrition .divider td { background: var(--brown); height: 20px; }
  .nutrition .gap td { height: 8px; }

  .print-space { left: 884px; width: 236px; height: 117px; background: #fff; display: flex; align-items: center; justify-content: center;
    font-size: 23px; color: #6e3a1a; }
  .best-before { top: 808px; }
  .barcode-space { top: 937px; }
</style>
</head>
<body>
<main class="label">
  <div class="abs label-body"></div>
  <div class="abs label-arch"></div>
  <div class="abs metal-band"></div>

  <div class="abs brand-name">BramliVex</div>
  <div class="abs mascot-art" role="img" aria-label="Brand mascot illustration holding a peanut"></div>

  <div class="abs social" style="top:310px"><span class="social-mark"></span>Chatterdesk</div>
  <div class="abs social" style="top:375px"><span class="social-mark"></span>Pictaloom</div>
  <div class="abs social" style="top:441px"><span class="social-mark"></span>Bramlivex.co.uk</div>

  <div class="abs eu-organic" role="img" aria-label="Organic certification badge"></div>

  <section class="abs info-box allergy">
    <h2>Allergy advice:</h2>
    <p>Peanuts are packed on<br>premises that handles<br>cereals, nuts (including<br>peanuts), soya, sesame &amp;<br>products containing<br>gluten.</p>
  </section>
  <section class="abs info-box storage">
    <h2>Storage Instructions:</h2>
    <p>Store in a cool, dry place<br>away from the light and<br>heat</p>
  </section>

  <div class="abs claim-organic">ORGANIC</div>
  <div class="abs claim-process">COLD PRESSED</div>
  <h1 class="abs product-name">Peanut Oil</h1>
  <div class="abs peanut-art" role="img" aria-label="Illustration of peanut leaves and an open peanut shell"></div>

  <div class="abs badge badge-vegan"><span class="b-top">100%</span><span class="b-main">VEGAN</span><span class="b-sub">FOOD</span></div>
  <div class="abs badge badge-organic"><span class="b-main">ORGANIC</span><span class="b-sub">FOOD</span></div>

  <div class="abs uk-mark" role="img" aria-label="Made in the UK badge"></div>
  <div class="abs volume">250ml</div>

  <div class="abs ingredients">Ingredients:<br>100% Organic<br>peanut oil</div>

  <section class="abs nutrition">
    <h3>Nutrition Information</h3>
    <table>
      <tr class="bar"><td>Typical values</td><td>per 100g</td></tr>
      <tr><td>Energy</td><td>kJ896/kCal3685</td></tr>
      <tr class="bar"><td>Fat</td><td>100g</td></tr>
      <tr class="sub"><td>Of which Saturated</td><td>19.7g</td></tr>
      <tr class="sub2"><td>Mono-unsaturated</td><td>36.4g</td></tr>
      <tr class="sub2"><td>Poly-unsaturated</td><td>43.4g</td></tr>
      <tr><td>Protein</td><td>0.1g</td></tr>
      <tr class="strong"><td>Carbohydrate</td><td>&lt;0.5g</td></tr>
      <tr class="divider"><td></td><td></td></tr>
      <tr class="gap"><td></td><td></td></tr>
      <tr><td>Fibre</td><td>&lt;0.5</td></tr>
    </table>
  </section>

  <div class="abs print-space best-before">best before date</div>
  <div class="abs print-space barcode-space">barcode</div>
</main>
</body>
</html>
```